VLO Nail Gel Polish Color Tip Swatch Label Design for SUN REEF collection

We need a label design for the color swatch that will go with our new collection of nail gel polish called SUN REEF. We are a nail and beauty supply distributor in the US selling to retail nail salons in the US only. Please also see our other project launched today: VLO Gel Nail Polish Collection for 15 ml bottle (Contest)

Target Market(s)

Retail Nail Salons in the US

Industry/Entity Type

Nail Salon

Font styles to use
Serif
Sans Serif

Colors

Designer to choose colors to be used in the design.

Requirements
Must have
• VLO Logo - this needs to be changed to all black color for letters VLO and matte gold drop for the "drop";
• SUN REEF in big font/easy to see;
• Numbers in big font/easy to see: CA1, CA2, .... CA16 on on side; and CA17, CA18, .... CA32 on the other side (as there will be 16 nail tips on each side).
• Label dimensions must be 1.875" x 9.0".
Nice to have
• possible additional wording, "Premium gel polish", "Collection"
Should not have
• no picture of SUN REEF; no overpowering graphics to make it look too busy

```html
<!DOCTYPE html>
<html lang="en">
<head>
<meta charset="utf-8">
<title>VLO Sun Reef Swatch Label</title>
<link rel="stylesheet" href="https://fonts.googleapis.com/css2?family=Open+Sans:wght@700&family=Tinos&display=swap">
<style>
  :root {
    --backdrop-light: #4a4a4a;
    --backdrop-dark: #262626;
    --label-tint: #e4e4e4;
    --accent-orange: #f26a1b;
    --ink: #222222;
    --silver-edge: #9c9c9c;
    --silver-mid: #ffffff;
    --drop-gold: #b8995a;
  }
  * { box-sizing: border-box; margin: 0; padding: 0; }
  html, body { width: 1200px; height: 1070px; overflow: hidden; }
  body {
    background: linear-gradient(135deg, var(--backdrop-light), var(--backdrop-dark));
    position: relative;
  }
  .swatch-label {
    position: absolute;
    left: 69px;
    top: 424px;
    width: 1061px;
    height: 222px;
    display: flex;
    flex-direction: column;
  }
  .number-row {
    height: 78px;
    background: var(--label-tint);
    display: grid;
    grid-template-columns: repeat(16, 1fr);
  }
  .number-row span {
    display: flex;
    align-items: center;
    justify-content: center;
    font-family: "Open Sans", sans-serif;
    font-weight: 700;
    font-size: 19px;
    line-height: 1;
    color: var(--ink);
    white-space: nowrap;
    writing-mode: vertical-rl;
    transform: rotate(180deg);
  }
  .title-band {
    height: 66px;
    border-top: 4px solid var(--accent-orange);
    border-bottom: 4px solid var(--accent-orange);
    background: linear-gradient(90deg, var(--silver-edge) 0%, #d6d6d6 25%, var(--silver-mid) 50%, #d6d6d6 75%, var(--silver-edge) 100%);
    position: relative;
    display: flex;
    align-items: center;
    justify-content: center;
  }
  .brand-mark {
    position: absolute;
    top: 50%;
    transform: translateY(-50%);
    display: flex;
    align-items: center;
    gap: 4px;
    font-family: "Tinos", serif;
    font-weight: 400;
    font-size: 34px;
    color: var(--ink);
    letter-spacing: -1px;
  }
  .brand-mark.left { left: 93px; }
  .brand-mark.right { right: 93px; }
  .brand-mark .drop {
    width: 13px;
    height: 13px;
    border-radius: 50%;
    background: var(--drop-gold);
  }
  .collection-title {
    font-family: "Tinos", serif;
    font-weight: 400;
    font-size: 37px;
    color: var(--ink);
    letter-spacing: 0.5px;
    white-space: nowrap;
  }
  .collection-title .name { color: var(--accent-orange); }
</style>
</head>
<body>
  <section class="swatch-label" aria-label="VLO Sun Reef premium gel polish swatch label">
    <div class="number-row upper">
      <span>CA17</span><span>CA18</span><span>CA19</span><span>CA20</span><span>CA21</span><span>CA22</span><span>CA23</span><span>CA24</span>
      <span>CA25</span><span>CA26</span><span>CA27</span><span>CA28</span><span>CA29</span><span>CA30</span><span>CA31</span><span>CA32</span>
    </div>
    <div class="title-band">
      <div class="brand-mark left">VLO<span class="drop"></span></div>
      <h1 class="collection-title"><span class="name">SUN REEF</span> PREMIUM GEL POLISH</h1>
      <div class="brand-mark right">VLO<span class="drop"></span></div>
    </div>
    <div class="number-row lower">
      <span>CA1</span><span>CA2</span><span>CA3</span><span>CA4</span><span>CA5</span><span>CA6</span><span>CA7</span><span>CA8</span>
      <span>CA9</span><span>CA10</span><span>CA11</span><span>CA12</span><span>CA13</span><span>CA14</span><span>CA15</span><span>CA16</span>
    </div>
  </section>
</body>
</html>
```